Lumora business card for a plastic surgeon

we need a business card for plastic surgeons that work on a clinic called LUMORA.
we want a clean design and the following informations: name of the doctor, doctor's registration number (called CRM), telephone, address, facebook, instagram.
Colors: white, blue tones, light brown/ coffee

facebook and instagram: lumoracirurgiaestetica

Industry/Entity Type

Business

Contact Information for Business Card

clean design

Font styles to use
Serif
Sans Serif
Other font styles liked:
• helvetica light

Colors
cee9f5
85cae6
85abd2
3276b5
cfeae6
cedeed
eaf1f7

Requirements
Must have
• doctor's name
• identification number (called CRM)
• contact (phone, facebook, instagram, address)

```html
<!DOCTYPE html>
<html lang="en">
<head>
<meta charset="utf-8">
<title>Lumora – Business Card</title>
<link rel="stylesheet" href="https://fonts.googleapis.com/css2?family=Cinzel:wght@400&family=Open+Sans:wght@400;600&display=swap">
<style>
  :root {
    --page-bg: #e9ecef;
    --card-white: #ffffff;
    --navy: #173a66;
    --cyan: #1bb3db;
    --cyan-light: #2fc0e3;
    --text-grey: #4f5459;
    --white: #ffffff;
  }
  * { margin: 0; padding: 0; box-sizing: border-box; }
  html, body {
    width: 1200px; height: 1000px; overflow: hidden;
    background: var(--page-bg);
  }
  .canvas { position: relative; width: 1200px; height: 1000px; }

  .card {
    position: absolute; left: 265px; width: 667px; height: 397px;
    border-radius: 24px; overflow: hidden;
    box-shadow: 0 6px 14px rgba(0,0,0,0.18);
  }
  .card--front { top: 73px; background: var(--card-white); }
  .card--back { top: 533px; background: var(--navy); }

  .front-wave { position: absolute; left: 0; top: 0; width: 667px; height: 397px; }

  .brand {
    position: absolute; font-family: "Cinzel", serif; font-weight: 400;
    color: var(--cyan); letter-spacing: 2px; white-space: nowrap;
    display: flex; align-items: center;
  }
  .brand__dot { border-radius: 50%; background: var(--cyan); margin-right: 14px; flex: none; }
  .card--front .brand { left: 34px; top: 128px; font-size: 54px; }
  .card--front .brand__dot { width: 16px; height: 16px; }
  .card--back .brand {
    left: 0; width: 667px; top: 110px; justify-content: center;
    font-size: 92px; color: var(--cyan-light);
  }
  .card--back .brand__dot { width: 24px; height: 24px; background: var(--cyan-light); }

  .person { position: absolute; left: 369px; top: 72px; font-family: "Open Sans", sans-serif; }
  .person__name { font-size: 26px; font-weight: 600; color: var(--cyan); line-height: 1.1; }
  .person__role { font-size: 17px; color: var(--text-grey); margin-top: 2px; line-height: 22px; }
  .person__crm { font-size: 14px; color: var(--text-grey); line-height: 20px; }

  .contacts {
    position: absolute; left: 369px; top: 172px; list-style: none;
    font-family: "Open Sans", sans-serif; font-size: 16px; color: var(--text-grey);
  }
  .contacts li { display: flex; align-items: center; height: 25px; }
  .contacts svg { width: 14px; height: 14px; margin-right: 8px; fill: var(--cyan); flex: none; }

  .address {
    position: absolute; left: 369px; top: 266px; font-style: normal;
    font-family: "Open Sans", sans-serif; font-size: 16px; line-height: 23px; color: var(--text-grey);
  }

  .social {
    position: absolute; left: 50px; top: 350px; display: flex; align-items: center;
    font-family: "Open Sans", sans-serif; font-size: 16px; font-weight: 600; color: var(--white);
  }
  .social__mark {
    width: 16px; height: 16px; background: var(--cyan-light); border-radius: 50%;
    margin-right: 10px; flex: none;
  }

  .back-url {
    position: absolute; left: 0; width: 667px; top: 347px; text-align: center;
    font-family: "Open Sans", sans-serif; font-size: 16px; color: var(--white);
  }
</style>
</head>
<body>
<div class="canvas">

  <section class="card card--front">
    <svg class="front-wave" viewBox="0 0 667 397" aria-hidden="true">
      <path d="M0 328 C 120 300, 250 302, 380 330 S 590 370 667 338 L667 397 L0 397 Z" fill="var(--cyan)"/>
      <path d="M0 344 C 130 318, 260 320, 390 348 S 590 378 667 352 L667 397 L0 397 Z" fill="var(--white)"/>
      <path d="M0 350 C 130 326, 260 328, 390 356 S 590 384 667 360 L667 397 L0 397 Z" fill="var(--navy)"/>
    </svg>

    <div class="brand"><span class="brand__dot"></span>LUMORA</div>

    <div class="person">
      <div class="person__name">Daniel Reyes</div>
      <div class="person__role">Surgeon</div>
      <div class="person__crm">CRM 000000</div>
    </div>

    <ul class="contacts">
      <li>
        <svg viewBox="0 0 16 16"><path d="M1 6 C1 3 4 2 8 2 S15 3 15 6 L12 7 L11 5 H5 L4 7 Z M3 8 H13 L14 14 H2 Z"/></svg>
        + 000 000 0000
      </li>
      <li>
        <svg viewBox="0 0 16 16"><path d="M1 3 H15 V13 H1 Z M1 3 L8 9 L15 3" stroke="var(--white)" stroke-width="1.2"/></svg>
        info@lumoracirurgiaestetica.com
      </li>
      <li>
        <svg viewBox="0 0 16 16"><circle cx="8" cy="8" r="7"/></svg>
        lumoracirurgiaestetica.com
      </li>
    </ul>

    <address class="address">
      4215 Harborview 9 Lane<br>
      Brooklyn, NewYork 11201
    </address>

    <div class="social"><span class="social__mark"></span>lumoracirurgiaestetica</div>
  </section>

  <section class="card card--back">
    <div class="brand"><span class="brand__dot"></span>LUMORA</div>
    <div class="back-url">lumoracirurgiaestetica.com</div>
  </section>

</div>
</body>
</html>
```